Website Design for Car Donations

Revise current site www.wheelsforheroes-sample.org

Sites i like:

https://www.autogiftbrigade.example

https://ridegivingcorps.example

https://protoboardly.example/7a2d91e4/screen/58217046

```html
<!DOCTYPE html>
<html lang="en">
<head>
<meta charset="utf-8">
<title>Wheels for Heroes – Donate Your Car</title>
<link rel="stylesheet" href="https://fonts.googleapis.com/css2?family=Roboto:wght@400;500;700;900&family=Open+Sans:wght@400;600;700&display=swap">
<style>
:root{
  --navy:#0b1f63;
  --navy-deep:#071548;
  --red:#c8141b;
  --ink:#2b2b2b;
  --field:#f1f1f1;
  --card:#f3f3f3;
  --white:#ffffff;
  --badge:#dfe4ee;
  --seal:#7fc0e6;
}
*{box-sizing:border-box;margin:0;padding:0}
html,body{width:1200px;height:2699px;overflow:hidden}
body{position:relative;background:var(--white);font-family:"Open Sans",Arial,sans-serif;color:var(--ink)}
.abs{position:absolute}

/* header */
.site-header{left:0;top:0;width:1200px;height:153px;background:linear-gradient(100deg,var(--navy-deep) 0%,var(--navy) 55%,#142a78 100%)}
.brand{display:flex;align-items:center;gap:12px}
.brand-dot{width:26px;height:26px;border-radius:50%;background:var(--red)}
.brand-name{font-family:"Roboto",sans-serif;font-weight:900;font-size:26px;color:var(--white);letter-spacing:.5px;white-space:nowrap}
.site-header .brand{left:80px;top:58px}
.main-nav{right:104px;top:56px;display:flex;align-items:center;gap:30px}
.main-nav a{font-family:"Roboto",sans-serif;font-weight:700;font-size:15px;color:var(--white);text-decoration:none;letter-spacing:.4px}
.main-nav .nav-cta{background:var(--red);padding:9px 22px;border-radius:3px}

/* hero */
.hero-photo{left:0;top:153px;width:774px;height:652px;background:linear-gradient(135deg,#c9b68e 0%,#9a8a68 40%,#6f6a55 70%,#3f4155 100%)}
.donate-panel{left:774px;top:153px;width:426px;height:652px;background:var(--white)}
.call-block{left:40px;top:24px;display:flex;gap:16px;align-items:center}
.call-icon{width:80px;height:80px;border:5px solid #333;border-radius:50%;display:flex;align-items:center;justify-content:center}
.call-label{font-family:"Roboto",sans-serif;font-weight:700;font-size:17px;letter-spacing:.5px;color:#333}
.call-number{font-family:"Roboto",sans-serif;font-weight:700;font-size:31px;color:#222;line-height:1.15}
.call-note{font-size:11px;font-weight:700;color:#333}
.car-tab{left:168px;top:118px;width:76px;height:56px;border-radius:38px 38px 0 0;background:var(--red);display:flex;justify-content:center;padding-top:10px}
.online-bar{left:30px;top:150px;width:346px;height:48px;background:var(--red);border-radius:6px;color:var(--white);font-family:"Roboto",sans-serif;font-weight:700;font-size:20px;letter-spacing:.6px;display:flex;align-items:center;justify-content:center}
.panel-sub{left:0;width:426px;top:216px;text-align:center;font-family:"Roboto",sans-serif;font-weight:700;font-size:17px;color:#333;letter-spacing:.3px}
.field{position:absolute;height:34px;background:var(--field);border-radius:4px;font-size:12px;color:#555;padding:0 18px;display:flex;align-items:center;justify-content:space-between}
.field .caret{width:0;height:0;border-left:5px solid transparent;border-right:5px solid transparent;border-top:7px solid #444}
.submit{left:40px;top:616px;width:336px;height:36px;background:var(--red);border-radius:5px;color:var(--white);font-family:"Roboto",sans-serif;font-weight:700;font-size:14px;letter-spacing:.5px;display:flex;align-items:center;justify-content:center}

/* benefits */
.section-title{width:1200px;left:0;text-align:center;font-family:"Roboto",sans-serif;font-weight:500;font-size:30px;letter-spacing:1px;color:#222}
.section-kicker{width:1200px;left:0;text-align:center;font-family:"Roboto",sans-serif;font-weight:500;font-size:15px;letter-spacing:1px;color:#333}
.benefits{left:88px;top:983px;display:flex;gap:12px}
.benefit{width:160px;height:138px;background:var(--card);border-radius:4px;display:flex;flex-direction:column;align-items:center;padding-top:22px;gap:12px;text-align:center;font-family:"Roboto",sans-serif;font-weight:500;font-size:14px;line-height:1.25;color:#333;letter-spacing:.4px}
.benefit svg{width:54px;height:44px}
.benefit.is-active{background:var(--red);color:var(--white)}

/* why */
.why-band{left:0;top:1188px;width:1200px;height:580px;background:linear-gradient(90deg,#f4f4f4 0%,#e9e9e9 60%,#f1f1f1 100%)}
.why-title{left:121px;top:1280px;font-family:"Roboto",sans-serif;font-weight:500;font-size:29px;letter-spacing:1px;color:#222}
.why-intro{left:121px;top:1326px;width:460px;font-family:"Roboto",sans-serif;font-weight:700;font-size:15px;line-height:1.4;color:#333}
.why-list{left:90px;top:1380px;width:500px;list-style:none}
.why-list li{position:relative;padding-left:31px;margin-bottom:20px;font-family:"Roboto",sans-serif;font-size:15px;line-height:1.35;color:#333;letter-spacing:.3px}
.why-list li::before{content:"";position:absolute;left:0;top:6px;width:10px;height:10px;border-radius:50%;background:var(--white)}
.why-list b{font-weight:700}
.why-photo{left:610px;top:1285px;width:504px;height:421px;background:linear-gradient(180deg,#7f9bb8 0%,#a3b4c4 45%,#7d7f6d 75%,#5f6353 100%)}

/* faq */
.faq-list{left:113px;top:1935px;width:512px;list-style:none}
.faq-list li{height:34px;margin-bottom:9px;background:var(--card);border-radius:3px;padding:0 14px;display:flex;align-items:center;justify-content:space-between;font-family:"Roboto",sans-serif;font-weight:500;font-size:15px;color:#333}
.faq-list .caret{width:0;height:0;border-left:5px solid transparent;border-right:5px solid transparent;border-top:7px solid #333}
.faq-photo{left:659px;top:1933px;width:425px;height:303px;background:linear-gradient(180deg,#4f6b3a 0%,#6f7f72 22%,#9aa3a6 55%,#7c7d78 80%,#5a5b56 100%)}

/* footer */
.site-footer{left:0;top:2322px;width:1200px;height:324px;background:linear-gradient(100deg,var(--navy-deep) 0%,var(--navy) 55%,#142a78 100%);color:var(--white)}
.site-footer .brand{left:120px;top:74px}
.footer-about{left:120px;top:130px;width:320px;font-family:"Roboto",sans-serif;font-weight:500;font-size:14px;line-height:1.35}
.footer-heading{font-family:"Roboto",sans-serif;font-weight:700;font-size:15px;letter-spacing:1px;padding-bottom:10px;border-bottom:3px solid var(--white);white-space:nowrap}
.footer-nav{left:494px;top:74px;width:104px}
.footer-nav ul{list-style:none;margin-top:16px}
.footer-nav li{font-family:"Roboto",sans-serif;font-weight:500;font-size:14px;letter-spacing:1px;margin-bottom:12px;white-space:nowrap}
.footer-secure{left:680px;top:74px;width:130px}
.badge-plate{position:absolute;left:0;top:58px;width:120px;height:44px;background:var(--badge);border-radius:6px}
.badge-seal{position:absolute;left:30px;top:118px;width:52px;height:52px;border-radius:50%;background:var(--seal);border:3px solid var(--white)}
.footer-call{left:882px;top:74px;width:204px;text-align:center}
.footer-call .footer-heading{text-align:left}
.footer-phone{margin-top:20px;display:flex;flex-direction:column;align-items:center}
.footer-phone .num{font-family:"Roboto",sans-serif;font-weight:700;font-size:26px;margin-top:10px;white-space:nowrap}
.footer-phone .note{font-family:"Roboto",sans-serif;font-weight:700;font-size:12px;line-height:1.25}

.copyright-bar{left:0;top:2646px;width:1200px;height:53px;background:var(--red);color:var(--white)}
.copyright-bar p{position:absolute;left:120px;top:16px;font-family:"Roboto",sans-serif;font-weight:700;font-size:16px;letter-spacing:.3px}
.social{position:absolute;right:108px;top:13px;display:flex;gap:10px}
.social span{width:27px;height:27px;border-radius:50%;background:var(--white)}
</style>
</head>
<body>

<header class="site-header abs">
  <div class="brand abs"><span class="brand-dot"></span><span class="brand-name">WHEELS FOR HEROES</span></div>
  <nav class="main-nav abs">
    <a href="#how">HOW TO DONATE</a>
    <a href="#why">WHY DONATE</a>
    <a href="#faq">FAQ</a>
    <a href="#about">ABOUT</a>
    <a class="nav-cta" href="#donate">DONATE NOW</a>
  </nav>
</header>

<div class="hero-photo abs" role="img" aria-label="Photo of a military family in camouflage uniforms holding a young child wrapped in an American flag"></div>

<section class="donate-panel abs" id="donate">
  <div class="call-block abs">
    <div class="call-icon">
      <svg width="40" height="40" viewBox="0 0 24 24"><path fill="#333" d="M6.6 10.8a15.2 15.2 0 0 0 6.6 6.6l2.2-2.2a1 1 0 0 1 1-.25 11.4 11.4 0 0 0 3.6.57 1 1 0 0 1 1 1V20a1 1 0 0 1-1 1A17 17 0 0 1 3 4a1 1 0 0 1 1-1h3.5a1 1 0 0 1 1 1c0 1.25.2 2.45.57 3.57a1 1 0 0 1-.25 1z"/></svg>
    </div>
    <div>
      <div class="call-label">CALL TODAY TO DONATE</div>
      <div class="call-number">1-800-555-0142</div>
      <div class="call-note">Live Operators Available - 7 Days A Week</div>
    </div>
  </div>
  <div class="car-tab abs">
    <svg width="32" height="26" viewBox="0 0 32 26"><path fill="#fff" d="M6 11l3-7h14l3 7h2v9h-3v3h-4v-3H11v3H7v-3H4v-9zm4.5-5L8.5 11h15l-2-5zM9 14a2 2 0 1 0 0 4 2 2 0 0 0 0-4zm14 0a2 2 0 1 0 0 4 2 2 0 0 0 0-4z"/></svg>
  </div>
  <div class="online-bar abs">DONATE YOUR CAR ONLINE</div>
  <div class="panel-sub abs">Full Tax Deduction - Running or Not</div>

  <div class="field" style="left:36px;top:268px;width:340px">First Name</div>
  <div class="field" style="left:36px;top:312px;width:340px">Last Name</div>
  <div class="field" style="left:36px;top:356px;width:340px">Phone</div>
  <div class="field" style="left:36px;top:400px;width:340px">Email</div>
  <div class="field" style="left:36px;top:444px;width:340px">Zip Code</div>
  <div class="field" style="left:36px;top:488px;width:166px">Choose Year <span class="caret"></span></div>
  <div class="field" style="left:208px;top:488px;width:168px">Choose Make <span class="caret"></span></div>
  <div class="field" style="left:36px;top:532px;width:340px">Vehicle Model</div>
  <div class="submit abs">DONATE NOW</div>
</section>

<section id="how">
  <h2 class="section-title abs" style="top:888px">DONATE YOUR CAR TO VETERANS</h2>
  <p class="section-kicker abs" style="top:930px">MAKE A DIFFERENCE</p>
  <div class="benefits abs">
    <div class="benefit">
      <svg viewBox="0 0 54 44" fill="none" stroke="#1c2a6b" stroke-width="2.5"><circle cx="14" cy="32" r="6"/><circle cx="28" cy="36" r="6"/><path d="M18 28L40 6M24 31L44 14"/><rect x="32" y="4" width="16" height="20" rx="2"/></svg>
      <span>YOU HAVE NO<br>COSTS</span>
    </div>
    <div class="benefit is-active">
      <svg viewBox="0 0 54 44" fill="none" stroke="#fff" stroke-width="2.5"><path d="M4 32V22h14l6-8h12l6 8h8v10z"/><circle cx="14" cy="34" r="4"/><circle cx="40" cy="34" r="4"/><path d="M42 22L50 6v8"/></svg>
      <span>FREE TOWING,<br>RUNNING OR NOT</span>
    </div>
    <div class="benefit">
      <svg viewBox="0 0 54 44" fill="none" stroke="#1c2a6b" stroke-width="2.5"><rect x="8" y="14" width="38" height="26" rx="2"/><path d="M8 14l19 14 19-14"/><rect x="16" y="4" width="22" height="18" fill="#fff"/><text x="27" y="18" font-size="12" text-anchor="middle" fill="#1c2a6b" stroke="none" font-family="Roboto,sans-serif" font-weight="700">$</text></svg>
      <span>WE ISSUE YOU AN<br>IRS TAX RECEIPT</span>
    </div>
    <div class="benefit">
      <svg viewBox="0 0 54 44" fill="none" stroke="#1c2a6b" stroke-width="2.5"><rect x="10" y="4" width="26" height="34" rx="2"/><path d="M15 12h16M15 18h16M15 24h10"/><circle cx="36" cy="26" r="9" fill="#fff"/><path d="M36 21v6M36 30v1M43 33l6 6"/></svg>
      <span>WE TAKE CARE OF<br>ALL PAPERWORK</span>
    </div>
    <div class="benefit">
      <svg viewBox="0 0 54 44" fill="none" stroke="#1c2a6b" stroke-width="2.5"><path d="M4 32V22l6-10h22l6 10v10z" fill="#1c2a6b"/><path d="M26 20l8 8 16-22" stroke-width="4"/></svg>
      <span>NO DMV<br>HASSLES</span>
    </div>
    <div class="benefit">
      <svg viewBox="0 0 54 44" fill="none" stroke="#1c2a6b" stroke-width="2.5"><rect x="4" y="6" width="46" height="30" rx="2"/><path d="M4 13h46"/><path d="M14 28v-6l4-5h16l4 5v6z" fill="#1c2a6b"/></svg>
      <span>VACATION<br>VOUCHER</span>
    </div>
  </div>
</section>

<section id="why">
  <div class="why-band abs"></div>
  <h2 class="why-title abs">WHY DONATE YOUR CAR TO US</h2>
  <p class="why-intro abs">IRS 501(c)3 Approved : Free 24/7 Pickup with No DMV Hassles.</p>
  <ul class="why-list abs">
    <li><b>arrow_iconFree Local Towing :</b> We will pick up your car donation, runningor not, when it's most convenient, at home or work.</li>
    <li><b>arrow_iconIncome Tax Deduction :</b> We issue you an IRS tax receipt and get you the highest tax write-off possible.</li>
    <li><b>arrow_iconNo Paperwork Hassles :</b> We handle everything: DMV and IRS paperwork.</li>
    <li><b>arrow_iconCar donations help fund programs :</b> And benefit Valor Path Foundation. An IRS 501(c)3 nonprofit organization.</li>
    <li><b>arrow_iconSchedule a Free Pickup :</b> Complete the form and a representative will call you to arrange a convenient time to pickup your car.</li>
  </ul>
  <div class="why-photo abs" role="img" aria-label="Photo of two soldiers in uniform smiling with a small girl holding an American flag"></div>
</section>

<section id="faq">
  <h2 class="section-title abs" style="top:1844px">FREQUENTLY ASKED QUESTIONS</h2>
  <ul class="faq-list abs">
    <li>What types of vehicles can be donated? <span class="caret"></span></li>
    <li>What paperwork do I need to donate my vehicle? <span class="caret"></span></li>
    <li>Is my donated vehicle tax-deductible? <span class="caret"></span></li>
    <li>What if the vehicle is not registered in my name? <span class="caret"></span></li>
    <li>How much will I receive as a tax deduction for my vehicle? <span class="caret"></span></li>
    <li>When will I receive my tax receipt? <span class="caret"></span></li>
    <li>How do I schedule a pick up? <span class="caret"></span></li>
  </ul>
  <div class="faq-photo abs" role="img" aria-label="Photo of a sports car painted with stars and stripes parked on a lakeside dock"></div>
</section>

<footer class="site-footer abs" id="about">
  <div class="brand abs"><span class="brand-dot"></span><span class="brand-name">WHEELS FOR HEROES</span></div>
  <p class="footer-about abs">Car donations help fund programs and benefit Valor Path Foundation. An IRS 501(c)3 nonprofit organization. Schedule a Free Pickup: Complete the form and a representative will call you to arrangea convenient time to pickup your car.</p>
  <div class="footer-nav abs">
    <div class="footer-heading">NAVIGATION</div>
    <ul><li>HOW TO DONATE</li><li>WHY DONATE</li><li>FAQ</li><li>ABOUT</li></ul>
  </div>
  <div class="footer-secure abs">
    <div class="footer-heading">SAFE &amp; SECURE</div>
    <div class="badge-plate" aria-label="Security badge"></div>
    <div class="badge-seal" aria-label="Approved charity seal"></div>
  </div>
  <div class="footer-call abs">
    <div class="footer-heading">CALL TODAY TO DONATE</div>
    <div class="footer-phone">
      <svg width="38" height="38" viewBox="0 0 38 38"><circle cx="19" cy="19" r="17" fill="none" stroke="#fff" stroke-width="2.5"/><path fill="#fff" transform="translate(9 9) scale(.85)" d="M6.6 10.8a15.2 15.2 0 0 0 6.6 6.6l2.2-2.2a1 1 0 0 1 1-.25 11.4 11.4 0 0 0 3.6.57 1 1 0 0 1 1 1V20a1 1 0 0 1-1 1A17 17 0 0 1 3 4a1 1 0 0 1 1-1h3.5a1 1 0 0 1 1 1c0 1.25.2 2.45.57 3.570a1 1 0 0 1-.25 1z"/></svg>
      <div class="num">1-800-555-0142</div>
      <div class="note">Live Operators Available<br>7 Days A Week</div>
    </div>
  </div>
</footer>

<div class="copyright-bar abs">
  <p>Copyright © 2018 WHEELS FOR HEROES.&nbsp; All Rights Reserved.</p>
  <div class="social"><span></span><span></span><span></span><span></span><span></span></div>
</div>

</body>
</html>
```